We need a cover designed for our book on parenting. The focus of this book is on the parents, not on the child! We like the idea of this title having a double meaning - insight as in gaining insights into parenting, and "in sight" as in looking inward as parents and how to improve ourselves rather than looking outward to improve our children. We would love for the cover to somehow represent this double meaning. I can upload an excerpt from the book soon over the next few days.
Updates

Reason: We are still reviewing the amazing designs! Thank you so much! :)

Target Market(s)

Parents with kids of any age from babies through adult children.

Requirements
Must have
• Title is: Harbor Parenting
• Subtitle is: Raising Families Through Reflection
• Authors names: Lena Morrow, LCSW Daniel Morrow, Ph.D.

```html
<!DOCTYPE html>
<html lang="en">
<head>
<meta charset="utf-8">
<title>Harbor Parenting — Book Cover</title>
<link rel="stylesheet" href="https://fonts.googleapis.com/css2?family=Anton&family=Crimson+Text&family=Cinzel:wght@400&display=swap">
<style>
  :root {
    --sky-top: #8fb0b8;
    --sky-mid: #a3bfc3;
    --mist: #b7cdcf;
    --spine-top: #7d9ba3;
    --spine-bottom: #8eaab0;
    --ink: #3b3a52;
    --band: #403e57;
    --band-text: #f1f0f4;
    --chair: #d9e4e6;
    --deck: #6f8590;
  }
  * { margin: 0; padding: 0; box-sizing: border-box; }
  html, body {
    width: 870px;
    height: 1200px;
    overflow: hidden;
    background: #ffffff;
  }
  .book {
    position: relative;
    width: 870px;
    height: 1200px;
    display: flex;
    overflow: hidden;
  }

  /* Spine */
  .spine {
    position: relative;
    width: 92px;
    height: 1200px;
    background: linear-gradient(180deg, var(--spine-top) 0%, var(--spine-bottom) 60%, #7f969e 100%);
    border-right: 2px solid #6f8b93;
  }
  .spine__title {
    position: absolute;
    top: 455px;
    left: 48px;
    writing-mode: vertical-rl;
    font-family: "Anton", "Oswald", sans-serif;
    font-size: 36px;
    line-height: 1;
    letter-spacing: 0.5px;
    color: var(--ink);
    text-transform: uppercase;
    white-space: nowrap;
  }
  .spine__authors {
    position: absolute;
    top: 250px;
    left: 12px;
    writing-mode: vertical-rl;
    font-family: "Crimson Text", "Georgia", serif;
    font-size: 27px;
    line-height: 1;
    color: var(--ink);
    white-space: nowrap;
  }
  .spine__band {
    position: absolute;
    left: 0;
    bottom: 0;
    width: 100%;
    height: 92px;
    background: #3a384f;
  }

  /* Front cover */
  .cover {
    position: relative;
    width: 778px;
    height: 1200px;
    background: linear-gradient(180deg, var(--sky-top) 0%, var(--sky-mid) 40%, var(--mist) 58%, var(--sky-mid) 100%);
    overflow: hidden;
  }
  .cover__title {
    position: absolute;
    top: 42px;
    left: 0;
    width: 100%;
    text-align: center;
    font-family: "Anton", "Oswald", sans-serif;
    color: var(--ink);
    text-transform: uppercase;
    font-weight: 400;
    line-height: 0.98;
    font-size: 168px;
    letter-spacing: 2px;
  }
  .cover__title span { display: block; }
  .cover__subtitle {
    position: absolute;
    top: 508px;
    left: 0;
    width: 100%;
    text-align: center;
    font-family: "Crimson Text", "Georgia", serif;
    font-size: 40px;
    color: var(--ink);
  }
  .cover__scene {
    position: absolute;
    top: 640px;
    left: 0;
    width: 778px;
    height: 468px;
    display: block;
  }
  .cover__band {
    position: absolute;
    left: 0;
    bottom: 0;
    width: 100%;
    height: 92px;
    background: var(--band);
    display: flex;
    align-items: center;
    justify-content: center;
  }
  .cover__authors {
    font-family: "Cinzel", "Times New Roman", serif;
    font-size: 29px;
    color: var(--band-text);
    letter-spacing: 0.3px;
    white-space: nowrap;
  }
</style>
</head>
<body>
  <div class="book">
    <aside class="spine">
      <p class="spine__title">Harbor Parenting</p>
      <p class="spine__authors">Lena Morrow, LCSW Daniel Morrow, Ph.D.</p>
      <div class="spine__band"></div>
    </aside>

    <main class="cover">
      <h1 class="cover__title">
        <span>Harbor</span>
        <span>Parenting</span>
      </h1>
      <p class="cover__subtitle">Raising Families Through Reflection</p>

      <svg class="cover__scene" viewBox="0 0 778 468" preserveAspectRatio="none" role="img"
           aria-label="Photo: two white Adirondack chairs and a small table on a rain-soaked wooden deck, with a teddy bear sitting on the table">
        <defs>
          <linearGradient id="sceneTone" x1="0" y1="0" x2="0" y2="1">
            <stop offset="0" stop-color="#a3bfc3" stop-opacity="0"/>
            <stop offset="0.3" stop-color="#c2d5d7"/>
            <stop offset="0.62" stop-color="#b3c7ca"/>
            <stop offset="0.8" stop-color="#8fa4ab"/>
            <stop offset="1" stop-color="#6f8590"/>
          </linearGradient>
        </defs>
        <rect x="0" y="0" width="778" height="468" fill="url(#sceneTone)"/>
      </svg>

      <footer class="cover__band">
        <p class="cover__authors">LENA MORROW, LCSW DANIEL MORROW, PH.D.</p>
      </footer>
    </main>
  </div>
</body>
</html>
```